Tamber Staffing teams up with Porlex

The spec:

This is an electronic invitation that will be sent to about 1000 potential attendees, but only a portion of these attendees will be able to come – so it is a first come first served.

What is the event?

The Willow Nations Trophy begins in May in England. We (Tamber Staffing) are hosting an event where we are hiring a cinema and will be flighting the South Africa vs Australia cricket match. The intention is to recreate a stadium atmosphere in South Africa to feel like we are at the game. There will be beer on tap, and stadium type food. Traditionally Australia is South Africa’s biggest rival and us beating them makes South Africans extremely happy

Who are we targeting?

This invitation is being sent to members of the Gauteng Trainee Ledger Guild (about 23 years old who are completing their CPA or Chartered Accountancy qualifications). They are young professionals but are closer to students with a salary.

Objective:

There should be less words and more pictures. People don’t want to spend ages reading the invitation. It needs to be short and to the point. The invitation will be sent out to the database by the committee of the association on our behalf. The recipient has got to understand that we are recreating the Stadium atmosphere in a cinema and its exclusively for Porlex (Gauteng trainee ledger members). The need to realise that its event that cannot be missed and that spots are limited and its on a first come first served basis.

A secondary message which we need to get across is the following, “This event is hosted and sponsored by Tamber Staffing, PORLEX’s new major partner. Tamber Staffing are the founders of the innovative new Ledgerly Hub (www.LedgerlyHub.co.zq) digital market place for newly qualified CAs.

The opening line needs to be eye-catching and the flyer needs to create interest immediately. Something along the lines of “PORLEX is bringing the Willow Nations Trophy to Sandton”

The main picture should be any image of SA team against Aus and potentially fans enjoying the spectacle. The main attraction needs to be the cricket match / Willow Nations Trophy.

Details:
• SA vs Australia
• Saturday 6th July
• 3:30pm
• Vell-Moranta’s exclusive cinema in Kramerville
• Beer-on-tap and Food provided
• Entrance is free – limited seats available and only Porlex Members
• Respond to this mail to secure your spot.

Target Market(s)

Industry/Entity Type

Recruitment

Font styles to use
Serif
Sans Serif

Colors
33a6d7
3176b5
cadf82
fee18a
deeab3
85cae6
cee9f5

Requirements
Must have
• The date, the time and the place.
• The sponsors (Tamber Staffing, Porlex and Vell-Moranta).
• • SA vs Australia
• • 6th July
• • 3:30pm
• • Vell-Moranta’s exclusive cinema
• • Beer on tap
• • A spit braai
Nice to have
• Lots of excitement and colour
Should not have
• Too many long sentences

```html
<!DOCTYPE html>
<html lang="en">
<head>
<meta charset="utf-8">
<title>Porlex – Willow Nations Trophy Screening Invitation</title>
<link rel="stylesheet" href="https://fonts.googleapis.com/css2?family=Alfa+Slab+One&family=Bitter:wght@400;600;700;800&display=swap">
<style>
  :root {
    --stage: #e6e6e6;
    --blue-deep: #1b63b8;
    --blue-mid: #3176b5;
    --blue-sky: #33a6d7;
    --navy: #163f7a;
    --navy-dark: #0f2f61;
    --lime: #cadf82;
    --lime-soft: #d6e396;
    --grass-light: #4cb83a;
    --grass: #2f9c2a;
    --grass-dark: #23841f;
    --red: #d8201f;
    --ink: #151515;
    --white: #ffffff;
  }
  * { margin: 0; padding: 0; box-sizing: border-box; }
  html, body {
    width: 1200px; height: 1200px; overflow: hidden;
    background: var(--stage);
  }
  .invitation {
    position: absolute; left: 190px; top: 20px;
    width: 820px; height: 1160px;
    box-shadow: 0 18px 40px rgba(0,0,0,0.25);
  }
  .invitation svg { display: block; }
  .display { font-family: "Alfa Slab One", serif; fill: var(--white); }
  .serif { font-family: "Bitter", serif; }
  .headline-soft { font-family: "Bitter", serif; font-weight: 400; fill: var(--white); }
  .match-title { font-family: "Alfa Slab One", serif; fill: var(--ink); }
  .match-vs { font-family: "Alfa Slab One", serif; fill: var(--white); }
  .match-date { font-family: "Bitter", serif; font-weight: 700; fill: var(--ink); }
  .venue { font-family: "Bitter", serif; font-weight: 700; fill: var(--white); }
  .entrance { font-family: "Bitter", serif; font-weight: 800; fill: var(--white); }
  .details { font-family: "Bitter", serif; font-weight: 400; fill: var(--white); }
  .badge-text { font-family: "Bitter", serif; font-weight: 400; fill: var(--white); }
  .sponsor { font-family: "Bitter", serif; font-weight: 700; fill: var(--navy); }
</style>
</head>
<body>
<div class="invitation">
  <svg width="820" height="1160" viewBox="0 0 820 1160" xmlns="http://www.w3.org/2000/svg">
    <defs>
      <linearGradient id="sky" x1="0" y1="0" x2="0" y2="1">
        <stop offset="0" stop-color="var(--blue-deep)"/>
        <stop offset="0.6" stop-color="var(--blue-sky)"/>
        <stop offset="1" stop-color="var(--blue-mid)"/>
      </linearGradient>
      <radialGradient id="grass" cx="0.5" cy="0" r="1">
        <stop offset="0" stop-color="var(--grass-light)"/>
        <stop offset="1" stop-color="var(--grass-dark)"/>
      </radialGradient>
      <linearGradient id="matchPhoto" x1="0" y1="0" x2="0" y2="1">
        <stop offset="0" stop-color="#4a4f57"/>
        <stop offset="0.55" stop-color="#6b6f3e"/>
        <stop offset="0.72" stop-color="#c2333b"/>
        <stop offset="1" stop-color="#3f7a3a"/>
      </linearGradient>
    </defs>

    <!-- backdrop -->
    <rect class="backdrop" width="820" height="1160" fill="url(#sky)"/>

    <!-- hero match photo -->
    <rect class="hero-frame" x="47" y="42" width="727" height="405" fill="var(--lime)"/>
    <rect class="hero-photo" x="56" y="52" width="709" height="386" fill="url(#matchPhoto)"
          role="img" aria-label="Photo of a South Africa vs Australia cricket match: batsman in yellow, wicketkeeper and bowler in green, crowd in the stands"/>

    <!-- headline -->
    <text class="display" x="392" y="567" font-size="78" text-anchor="end">PORLEX</text>
    <text class="headline-soft" x="657" y="564" font-size="38" text-anchor="end">is bringing</text>
    <text class="display" x="657" y="634" font-size="40" text-anchor="end">the Willow Nations Trophy</text>
    <circle class="helmet-sa" cx="216" cy="689" r="30" fill="var(--grass)"
            role="img" aria-label="South African cricket helmet"/>
    <circle class="helmet-aus" cx="311" cy="689" r="30" fill="#f2c230"
            role="img" aria-label="Australian cricket helmet"/>
    <text class="display" x="657" y="704" font-size="50" text-anchor="end">to Sandton</text>

    <!-- stadium band -->
    <polygon class="stadium-band" points="0,753 300,775 520,775 820,753 820,918 0,918" fill="var(--navy)"/>
    <polygon class="stadium-band-edge" points="0,800 300,815 520,815 820,800 820,810 520,825 300,825 0,810" fill="var(--navy-dark)"/>

    <!-- match strip -->
    <polygon class="match-strip" points="122,786 190,770 480,768 700,776 690,800 712,826 684,852 706,880 660,900 420,906 150,902 118,880 140,856 112,830 136,806"
             fill="var(--lime-soft)"/>
    <text class="match-title" x="222" y="834" font-size="44" text-anchor="middle">SA</text>
    <circle class="vs-ball" cx="338" cy="811" r="34" fill="var(--red)"/>
    <text class="match-vs" x="338" y="825" font-size="34" text-anchor="middle">VS</text>
    <text class="match-title" x="383" y="834" font-size="44">Australia</text>
    <text class="match-date" x="410" y="882" font-size="26" text-anchor="middle">Saturday 6th July • 3:30pm</text>

    <!-- field -->
    <path class="field" d="M0,918 Q410,896 820,918 L820,1160 L0,1160 Z" fill="url(#grass)"/>

    <!-- details -->
    <text class="venue" x="61" y="957" font-size="19">Vell-Moranta’s exclusive cinema in Kramerville</text>
    <text class="entrance" x="61" y="991" font-size="27">Entrance</text>
    <text class="entrance" x="63" y="1021" font-size="27">is FREE -</text>
    <rect class="divider" x="199" y="972" width="1.5" height="48" fill="var(--white)"/>
    <text class="details" x="216" y="1011" font-size="16">limited seats available and only Porlex Members</text>
    <text class="details" x="216" y="1036" font-size="16">Respond to this mail to secure your spot.</text>

    <!-- perk badge -->
    <circle class="perk-badge" cx="696" cy="1016" r="64" fill="var(--red)" stroke="var(--white)" stroke-width="2"/>
    <text class="badge-text" x="696" y="1014" font-size="14.5" text-anchor="middle">Beer-on-tap and</text>
    <text class="badge-text" x="696" y="1032" font-size="14.5" text-anchor="middle">Food provided</text>

    <!-- sponsors -->
    <path class="sponsor-tab" d="M161,1160 L161,1106 Q161,1086 181,1086 L640,1086 Q660,1086 660,1106 L660,1160 Z" fill="var(--white)"/>
    <rect x="208" y="1116" width="14" height="14" fill="var(--navy)"/>
    <text class="sponsor" x="228" y="1129" font-size="14">Tamber Staffing</text>
    <text class="sponsor" x="412" y="1129" font-size="14" text-anchor="middle">Porlex</text>
    <rect x="494" y="1116" width="14" height="14" fill="var(--navy)"/>
    <text class="sponsor" x="514" y="1129" font-size="14">Vell-Moranta</text>
  </svg>
</div>
</body>
</html>
```